Book cover (front only) for proposal by established author

We need a book cover design - must be inspirational, credible, powerful, noticeable - for a self-help book being written by an established author (15 books with major publishers). Front cover only. This will be used in a proposal being sent to a literary agent; it's NOT for publication, so high-res is NOT needed. We are providing a draft design in a doc format, but you have complete freedom with the graphics, colors, and fonts. Final product should be a pdf file, unless you have a better suggestion.

```html
<!DOCTYPE html>
<html lang="en">
<head>
<meta charset="utf-8">
<title>See How We Rise – Book Cover</title>
<link href="https://fonts.googleapis.com/css2?family=Montserrat:wght@700&family=Open+Sans:ital,wght@0,400;1,600;1,700&display=swap" rel="stylesheet">
<style>
  :root {
    --paper: #ffffff;
    --cover: #ffffff;
    --amber-band: #f7a21b;
    --sand: #fbe0b8;
    --sand-light: #fdeedb;
    --navy: #0b3a7c;
    --title-navy: #123f86;
    --title-accent: #f0581a;
    --ink: #151515;
  }
  html, body {
    margin: 0;
    padding: 0;
    width: 1200px;
    height: 1200px;
    overflow: hidden;
    background: var(--paper);
  }
  .stage {
    position: relative;
    width: 1200px;
    height: 1200px;
  }
  .cover-art {
    position: absolute;
    inset: 0;
    width: 1200px;
    height: 1200px;
  }
  .title {
    position: absolute;
    left: 232px;
    top: 145px;
    margin: 0;
    font-family: "Montserrat", "Arial Black", sans-serif;
    font-weight: 700;
    font-size: 150px;
    line-height: 172px;
    letter-spacing: 2px;
    color: var(--title-navy);
  }
  .title span { display: block; }
  .title .word-accent { color: var(--title-accent); }
  .subtitle {
    position: absolute;
    left: 217px;
    top: 908px;
    width: 820px;
    margin: 0;
    font-family: "Open Sans", "Calibri", sans-serif;
    font-size: 21px;
    line-height: 30px;
    color: var(--navy);
  }
  .tagline {
    position: absolute;
    left: 217px;
    top: 978px;
    width: 820px;
    margin: 0;
    font-family: "Open Sans", "Calibri", sans-serif;
    font-style: italic;
    font-weight: 600;
    font-size: 21.5px;
    line-height: 38px;
    color: var(--navy);
  }
  .author {
    position: absolute;
    right: 204px;
    top: 1100px;
    margin: 0;
    font-family: "Open Sans", "Calibri", sans-serif;
    font-style: italic;
    font-weight: 700;
    font-size: 40px;
    color: var(--ink);
  }
</style>
</head>
<body>
<main class="stage">
  <svg class="cover-art" viewBox="0 0 1000 1000" aria-hidden="true">
    <rect class="cover-sheet" x="157" y="30" width="713" height="940" fill="var(--cover)"/>
    <path class="top-band" d="M157,30 H870 V300 C790,190 640,108 440,104 C330,102 230,110 157,118 Z" fill="var(--amber-band)"/>
    <path class="arc-thin" d="M157,290 C215,520 420,750 870,820 L870,840 C420,780 200,560 157,335 Z" fill="var(--sand-light)"/>
    <path class="arc-main" d="M157,550 C235,730 405,848 605,888 C695,902 790,882 870,838 V970 H157 Z" fill="var(--sand)"/>
    <path class="lower-panel" d="M157,860 H830 V970 H157 Z" fill="var(--sand)"/>
  </svg>

  <h1 class="title">
    <span>SEE</span>
    <span>HOW</span>
    <span>WE</span>
    <span class="word-accent">RISE</span>
  </h1>

  <p class="subtitle">Closer in Our Friendships, Kinder Partners, More Active, More Curious,<br>More Focused, More Patient, and More Deeply Content</p>

  <p class="tagline">A veteran behavioral scientist reveals the capacity each of us has<br>to think and live better in every corner of our daily lives.</p>

  <p class="author">Daniel Hartwell, Ph.D.</p>
</main>
</body>
</html>
```